Business Card Design Project

Hi
I'm currently getting a logo designed which will go on the front. It is designed for s
Fitness instructor/ personal training business.
On the back I would like written:
Boxing for Fitness
Aqua Fitness Professional
PersonalisedTraining 1/1 or Small Group outdoor training
Fun and unique workouts
Weight loss/ Strength training

Also I need on there my details
minaharker27@quellmail.net
0438 917 355
FB Mina Fitness

Reason: I would like to extend the deadline to give extra days after I have confirmed the logo in two days

Target Market(s)

Mostly women aged between 20-50

Industry/Entity Type

Training

Font styles to use
Sans Serif

Requirements
Must have
• My logo ( I have attached my favourite logo options )
My details

```html
<!DOCTYPE html>
<html lang="en">
<head>
<meta charset="utf-8">
<title>Mina Fitness – Business Cards</title>
<link href="https://fonts.googleapis.com/css2?family=Montserrat:wght@600;700&family=Arvo:wght@700&display=swap" rel="stylesheet">
<style>
  :root {
    --page-bg: #ececec;
    --card-white: #ffffff;
    --brand-blue: #4cc3ee;
    --ink-dark: #1a1a1a;
    --ink-white: #ffffff;
    --divider-blue: #4cc3ee;
    --social-square: #2f5ea8;
  }
  * { margin: 0; padding: 0; box-sizing: border-box; }
  html, body {
    width: 1200px; height: 900px; overflow: hidden;
    background: var(--page-bg);
  }
  .canvas { position: relative; width: 1200px; height: 900px; }

  .card {
    position: absolute; left: 285px; width: 630px; height: 360px;
    box-shadow: 0 6px 18px rgba(0,0,0,0.18);
    overflow: hidden;
  }
  .card--front { top: 70px; background: var(--card-white); }
  .card--back  { top: 470px; background: var(--brand-blue); }

  .brand-mark {
    position: absolute; display: flex; align-items: center; gap: 12px;
    font-family: "Montserrat", sans-serif; font-weight: 700;
    letter-spacing: 0.5px; white-space: nowrap;
  }
  .brand-mark__circle {
    border-radius: 50%; border: 4px solid currentColor; flex: none;
  }
  .card--front .brand-mark {
    color: var(--brand-blue); left: 50%; top: 88px;
    transform: translateX(-50%); font-size: 42px;
  }
  .card--front .brand-mark__circle { width: 70px; height: 70px; }
  .card--back .brand-mark {
    color: var(--ink-white); left: 40px; top: 145px; font-size: 30px;
  }
  .card--back .brand-mark__circle { width: 56px; height: 56px; }

  .service-list {
    position: absolute; left: 10px; right: 10px; bottom: 50px;
    font-family: "Montserrat", sans-serif; font-weight: 700;
    font-size: 9px; letter-spacing: 0.4px; text-transform: uppercase;
    color: var(--ink-dark); text-align: center; line-height: 22px;
    white-space: nowrap;
  }
  .service-list__sep {
    display: inline-block; width: 2px; height: 12px; margin: 0 8px;
    background: var(--divider-blue); vertical-align: -2px;
  }

  .back-divider {
    position: absolute; left: 345px; top: 110px; width: 4px; height: 120px;
    background: var(--ink-dark);
  }
  .contact {
    position: absolute; left: 365px; top: 112px;
    font-family: "Arvo", serif; font-weight: 700;
    font-size: 15px; line-height: 22px; color: var(--ink-white);
    white-space: nowrap;
  }
  .social {
    position: absolute; left: 290px; top: 275px; display: flex; align-items: center; gap: 12px;
    font-family: "Arvo", serif; font-weight: 700; font-size: 18px; color: var(--ink-white);
  }
  .social__square {
    width: 24px; height: 24px; background: var(--social-square); border: 2px solid var(--ink-white);
  }
</style>
</head>
<body>
<main class="canvas">
  <section class="card card--front" aria-label="Card front">
    <div class="brand-mark"><span class="brand-mark__circle"></span>Mina Fitness</div>
    <div class="service-list">
      <div>Boxing for Fitness<span class="service-list__sep"></span>Aqua Fitness Professional<span class="service-list__sep"></span>1/1 or Small Group Outdoor Training</div>
      <div>Fun and Unique Workouts<span class="service-list__sep"></span>Weight Loss/ Strength Training<span class="service-list__sep"></span>Personalised Training</div>
    </div>
  </section>

  <section class="card card--back" aria-label="Card back">
    <div class="brand-mark"><span class="brand-mark__circle"></span>Mina Fitness</div>
    <div class="back-divider"></div>
    <div class="contact">
      <div class="contact__email">minaharker27@quellmail.net</div>
      <div class="contact__phone">0438 917 355</div>
    </div>
    <div class="social"><span class="social__square"></span>Mina Fitness</div>
  </section>
</main>
</body>
</html>
```